Japanese Rice Food Package Label

- We are launching Japanese food products to the outdoor community.
- Made in Japan
- We will have multiple flavors of rice but want to keep the package label almost the same and only replace the flavor text (e.g., Mixed Rice, Curry Rice, etc)
- We like simple designs inspired by Japan.
- Label size: 105 mm x148 mm
- Our brand: YOBEN https://yoben.co/
- Video message: https://www.vidqo.com/share/3f51b07a9e2c4d6891a0c7e5b2d94f18

```html
<!DOCTYPE html>
<html lang="en">
<head>
<meta charset="utf-8">
<title>YOBEN Mixed Rice Label</title>
<link rel="stylesheet" href="https://fonts.googleapis.com/css2?family=Special+Elite&family=Montserrat:wght@500;900&display=swap">
<style>
  :root {
    --page: #ffffff;
    --label-cream: #fdfaf1;
    --ink: #111111;
    --ink-soft: #3a3a3a;
    --flavor-fill: #e0bb98;
    --stalk-light: #e9e6de;
    --stalk-mid: #b9b8b2;
    --stalk-dark: #7d7e7a;
  }
  * { margin: 0; padding: 0; box-sizing: border-box; }
  html, body {
    width: 1200px;
    height: 1200px;
    overflow: hidden;
    background: var(--page);
  }
  .canvas {
    position: relative;
    width: 1200px;
    height: 1200px;
  }
  .label {
    position: absolute;
    left: 60px;
    top: 233px;
    width: 1080px;
    height: 734px;
    background: var(--label-cream);
    overflow: hidden;
  }
  .rice-stalks {
    position: absolute;
    left: 0;
    top: 0;
    width: 320px;
    height: 734px;
    background: linear-gradient(100deg, var(--stalk-mid) 0%, var(--stalk-light) 55%, var(--label-cream) 100%);
    opacity: 0.8;
  }
  .flavor-badge {
    position: absolute;
    left: 325px;
    top: 155px;
    width: 390px;
    height: 390px;
  }
  .flavor-name {
    position: absolute;
    left: 325px;
    top: 155px;
    width: 390px;
    height: 390px;
    display: flex;
    flex-direction: column;
    justify-content: center;
    align-items: center;
    font-family: "Special Elite", "Courier New", monospace;
    font-size: 68px;
    line-height: 1.25;
    color: var(--ink);
    text-align: center;
  }
  .origin {
    position: absolute;
    left: 220px;
    width: 600px;
    top: 632px;
    text-align: center;
    font-family: "Montserrat", Arial, sans-serif;
    font-weight: 500;
    font-size: 30px;
    letter-spacing: 4px;
    line-height: 38px;
    color: var(--ink-soft);
  }
  .brand-name {
    position: absolute;
    left: 932px;
    top: 363px;
    transform: translate(-50%, -50%) rotate(-90deg);
    font-family: "Montserrat", Arial, sans-serif;
    font-weight: 900;
    font-size: 182px;
    line-height: 1;
    letter-spacing: 4px;
    color: var(--ink);
    white-space: nowrap;
  }
</style>
</head>
<body>
  <div class="canvas">
    <div class="label">
      <div class="rice-stalks" role="img" aria-label="Line drawing of rice stalks and grass blades"></div>

      <svg class="flavor-badge" viewBox="0 0 390 390" aria-hidden="true">
        <circle cx="195" cy="195" r="184" fill="var(--flavor-fill)"/>
        <circle cx="195" cy="195" r="191" fill="none" stroke="var(--ink)" stroke-width="4"/>
      </svg>
      <div class="flavor-name">
        <span>Mixed</span>
        <span>Rice</span>
      </div>

      <p class="origin">Made in Japan<br>yoben.co</p>

      <div class="brand-name">YOBEN</div>
    </div>
  </div>
</body>
</html>
```